Diverse, up-scale salon needs eye-catching, unique business cards.

We are looking for a unique business card design for our stylist but that can also be multi functional and used for appointment reminder and referrals. I will need a design in a format that I can modify names and titles going forward. In the past we have had a dark background with the logo on one side, and stylist and contact information on the other but we are open to all ideas. I have included our mission statement as well as branded colors below. The statement doesn't need to go on the card, it's just a reference for target market. We need space for the stylists name, title, instagram handle and then the salons phone number, website and address. I am also open to adding a spot for a qr code linked to the stylist instagram or the salon booking link.

primary brand colors:
#333333 #233415 #36502a #93874a #000000
Mission statement:
Venturo Mane Studio, a high-end salon located in the lively Downtown Farmington, Michigan, is committed to providing exceptional services in a welcoming and relaxed environment to meet the needs of our diverse clientele.
Our salon specializes in contemporary custom haircuts, coloring, extensions, and barbering and beard grooming services. Our team of skilled stylists is passionate and inventive in their hair styling techniques. At the heart of our salon are values centered on quality, innovation, creativity, and above all, comfort. These core values are evident in every appointment across our customizable array of services.
Our goal is to establish a benchmark for exceptional hair care for every human.
Website: www.venturomanestudio.example
instagram: @venturomanestudio
address: 18720 Willowcrest Blvd, Farmington MI
phone: 248-316-7408

Industry/Entity Type

Hair Salon

Contact Information for Business Card

Stylist name, title, phone, instagram, website, address, (optional qr code)

Requirements
Should not have
• Does not need mission statement on the card.

```html
<!DOCTYPE html>
<html lang="en">
<head>
<meta charset="utf-8">
<title>Venturo Mane Studio – Stylist Business Card</title>
<link rel="stylesheet" href="https://fonts.googleapis.com/css2?family=Arimo:wght@400;700&family=Teko:wght@600&display=swap">
<style>
  :root {
    --backdrop: #979797;
    --card: #242424;
    --emboss-line: #1b1b1b;
    --emboss-text: #1d1d1d;
    --faint-mark: #2d2d2d;
    --gold: #93874a;
    --ink-light: #ffffff;
    --icon-glyph: #242424;
  }
  * { margin: 0; padding: 0; box-sizing: border-box; }
  html, body {
    width: 1200px; height: 1200px; overflow: hidden;
    background: var(--backdrop);
  }
  .stage { position: relative; width: 1200px; height: 1200px; }

  .card {
    position: absolute;
    top: 215px;
    width: 437px;
    height: 746px;
    border-radius: 25px;
    background: var(--card);
    overflow: hidden;
  }
  .card--front { left: 122px; }
  .card--back  { left: 587px; }

  /* Front: emblem area */
  .emblem {
    position: absolute;
    left: 71px; top: 228px;
    width: 290px; height: 290px;
    border: 4px solid var(--emboss-line);
    border-radius: 50%;
    display: flex; align-items: center; justify-content: center;
    text-align: center;
  }
  .emblem__name {
    font-family: "Arimo", sans-serif;
    font-weight: 700;
    font-size: 30px;
    line-height: 1.2;
    letter-spacing: 2px;
    text-transform: uppercase;
    color: var(--emboss-text);
  }

  /* Back: stylist details */
  .details {
    position: absolute;
    left: 0; right: 0; top: 208px;
    text-align: center;
    color: var(--ink-light);
    font-family: "Arimo", sans-serif;
    font-size: 19.5px;
    line-height: 22.5px;
  }
  .stylist-name {
    display: inline-block;
    border: 3px solid var(--ink-light);
    padding: 5px 0 0;
    width: 140px; height: 52px;
    font-family: "Teko", sans-serif;
    font-weight: 600;
    font-size: 38px;
    line-height: 44px;
    letter-spacing: 1px;
    text-transform: uppercase;
  }
  .icon-row {
    display: flex; justify-content: center; gap: 6px;
    margin: 26px 0 7px;
  }
  .icon-row--single { margin: 8px 0 5px; }
  .icon-row--location { margin-top: 12px; }
  .icon {
    width: 24px; height: 24px;
    border-radius: 50%;
    background: var(--gold);
    display: flex; align-items: center; justify-content: center;
  }
  .icon svg { width: 14px; height: 14px; fill: var(--icon-glyph); }
  .contact-line { display: block; }
  .address { margin-top: 2px; }

  .faint-mark {
    position: absolute;
    left: -6px; bottom: 20px;
    font-family: "Arimo", sans-serif;
    font-weight: 700;
    font-size: 96px;
    line-height: 1;
    white-space: nowrap;
    color: var(--faint-mark);
  }
</style>
</head>
<body>
<main class="stage">

  <section class="card card--front" aria-label="Card front">
    <div class="emblem">
      <span class="emblem__name">Venturo<br>Mane<br>Studio</span>
    </div>
  </section>

  <section class="card card--back" aria-label="Card back">
    <div class="details">
      <h1 class="stylist-name">Rowan</h1>

      <div class="icon-row" aria-hidden="true">
        <span class="icon"><svg viewBox="0 0 24 24"><path d="M6.6 10.8a15.1 15.1 0 0 0 6.6 6.6l2.2-2.2a1 1 0 0 1 1-.25 11.4 11.4 0 0 0 3.6.57 1 1 0 0 1 1 1V20a1 1 0 0 1-1 1A17 17 0 0 1 3 4a1 1 0 0 1 1-1h3.5a1 1 0 0 1 1 1c0 1.25.2 2.45.57 3.57a1 1 0 0 1-.25 1z"/></svg></span>
        <span class="icon"><svg viewBox="0 0 24 24"><path d="M3 5h18a1 1 0 0 1 1 1v12a1 1 0 0 1-1 1H3a1 1 0 0 1-1-1V6a1 1 0 0 1 1-1zm9 7.5L20 7H4z"/></svg></span>
        <span class="icon"><svg viewBox="0 0 24 24"><path d="M12 2a10 10 0 1 0 0 20 10 10 0 0 0 0-20zm6.9 6h-2.9a15.7 15.7 0 0 0-1.4-3.6A8 8 0 0 1 18.9 8zM12 4c.8 1.2 1.5 2.5 1.9 4h-3.8c.4-1.5 1.1-2.8 1.9-4zM4.3 14a8.2 8.2 0 0 1 0-4h3.4a16 16 0 0 0 0 4zm.8 2h2.9a15.7 15.7 0 0 0 1.4 3.6A8 8 0 0 1 5.1 16zM8 8H5.1a8 8 0 0 1 4.3-3.6A15.7 15.7 0 0 0 8 8zm4 12c-.8-1.2-1.5-2.5-1.9-4h3.8c-.4 1.5-1.1 2.8-1.9 4zm2.3-6H9.7a14.7 14.7 0 0 1 0-4h4.6a14.7 14.7 0 0 1 0 4zm.3 5.6a15.7 15.7 0 0 0 1.4-3.6h2.9a8 8 0 0 1-4.3 3.6zm1.7-5.6a16 16 0 0 0 0-4h3.4a8.2 8.2 0 0 1 0 4z"/></svg></span>
      </div>
      <span class="contact-line">(248) 316-7408</span>
      <span class="contact-line">hello@venturomanestudio.example</span>
      <span class="contact-line">venturomanestudio.example</span>

      <div class="icon-row icon-row--single" aria-hidden="true">
        <span class="icon"><svg viewBox="0 0 24 24"><rect x="4" y="4" width="16" height="16" rx="2"/></svg></span>
      </div>
      <span class="contact-line">venturomanestudio</span>

      <div class="icon-row icon-row--single icon-row--location" aria-hidden="true">
        <span class="icon"><svg viewBox="0 0 24 24"><path d="M12 2a7 7 0 0 0-7 7c0 5.2 7 13 7 13s7-7.8 7-13a7 7 0 0 0-7-7zm0 9.5A2.5 2.5 0 1 1 12 6.5a2.5 2.5 0 0 1 0 5z"/></svg></span>
      </div>
      <span class="contact-line address">18720 Willowcrest Blvd</span>
      <span class="contact-line">Hollisford Michigan</span>
    </div>

    <span class="faint-mark" aria-hidden="true">Venturo</span>
  </section>

</main>
</body>
</html>
```